Drifting Past Solvane website

A very basic website using the graphics provided. The site would give the user the ability to read a description of the book, read testimonials, About the author, Read chapter 1, link to vendoro, order direct via coinlet.

```html
<!DOCTYPE html>
<html lang="en">
<head>
<meta charset="utf-8">
<title>Drifting Past Solvane</title>
<link rel="stylesheet" href="https://fonts.googleapis.com/css2?family=Open+Sans:wght@400;600;700&family=Roboto+Slab:wght@400&display=swap">
<style>
:root{
  --bar:#050304;
  --hero-dark:#1e1012;
  --hero-mid:#3a2225;
  --hero-glow:#4a2a2e;
  --ink:#1c1c1c;
  --rose:#a0666c;
  --rose-soft:#a87f83;
  --gold:#d9a33a;
  --cta:#b6643a;
  --white:#ffffff;
  --rule:#ececec;
  --footer:#221316;
  --frame:#1a1a1a;
}
*{margin:0;padding:0;box-sizing:border-box}
html,body{width:1081px;height:1200px;overflow:hidden;background:var(--white)}
body{position:relative;font-family:"Open Sans",Arial,sans-serif;color:var(--ink)}
.site-header{position:absolute;left:0;top:0;width:1081px;height:84px;background:var(--bar);box-shadow:0 2px 6px rgba(0,0,0,.6);z-index:2}
.nav-link{position:absolute;top:56px;transform:translate(-50%,-50%);color:var(--white);font-size:13px;text-transform:uppercase;letter-spacing:.2px;white-space:nowrap}
.brand{position:absolute;left:540px;top:50px;transform:translate(-50%,-50%);font-family:"Open Sans",Arial,sans-serif;font-weight:600;color:var(--gold);font-size:18px;letter-spacing:.5px;white-space:nowrap}
.hero{position:absolute;left:0;top:84px;width:1081px;height:513px;background:radial-gradient(ellipse 55% 70% at 28% 45%,var(--hero-glow),var(--hero-mid) 45%,var(--hero-dark) 100%)}
.book-cover{position:absolute;left:161px;top:174px;width:273px;height:410px;background:linear-gradient(180deg,#3b1519 0%,#5a2a2c 22%,#6d8a94 40%,#2a2a2a 70%,#0e0a0a 100%);border-right:5px solid #d8d8d8;border-top:4px solid #e6e6e6;box-shadow:6px 0 10px rgba(0,0,0,.4)}
.shelf{position:absolute;left:128px;top:584px;width:351px;height:8px;border-radius:4px;background:linear-gradient(180deg,#f5f5f5,#a9a9a9)}
.shelf-peg{position:absolute;top:590px;width:7px;height:12px;background:#cfcfcf;border-radius:2px}
.hero-kicker{position:absolute;left:540px;top:183px;font-size:16px;color:#e4dcdc}
.hero-title{position:absolute;left:540px;top:208px;font-family:"Roboto Slab",Georgia,serif;font-weight:400;font-size:33px;line-height:44px;color:var(--white);letter-spacing:.3px;white-space:nowrap}
.hero-quote{position:absolute;left:540px;top:274px;width:405px;font-size:15.5px;line-height:25.2px;color:var(--rose-soft)}
.buy-button{position:absolute;left:540px;top:430px;width:190px;height:41px;border-radius:4px;background:var(--cta);color:var(--white);font-weight:700;font-size:16px;display:flex;align-items:center;justify-content:center}
.section-title{position:absolute;left:127px;font-size:19px;font-weight:400;color:var(--ink)}
.about-text{position:absolute;left:127px;top:692px;width:657px;font-size:12.6px;line-height:25.2px;color:var(--rose);text-align:justify}
.author-photo{position:absolute;left:809px;top:698px;width:145px;height:147px;border:4px solid var(--frame);outline:1px solid #ccc;background:linear-gradient(160deg,#6a4a32,#9b6a54 50%,#3a2c22)}
.divider{position:absolute;left:127px;top:888px;width:827px;height:1px;background:var(--rule)}
.testimonial{position:absolute;top:978px;width:400px;height:80px}
.testimonial-photo{position:absolute;left:0;top:0;width:77px;height:78px;border:3px solid #e8e8e8;background:linear-gradient(180deg,#d9dde0,#8c8f94 60%,#2d3035)}
.testimonial-pointer{position:absolute;left:77px;top:28px;width:0;height:0;border-top:10px solid transparent;border-bottom:10px solid transparent;border-left:10px solid #e8e8e8}
.testimonial-text{position:absolute;left:108px;top:0;width:290px;font-size:11.5px;line-height:20.4px;color:var(--rose)}
.testimonial-name{position:absolute;left:108px;top:70px;font-size:11.5px;color:var(--ink)}
.slider-dots{position:absolute;left:529px;top:1064px;display:flex;gap:3px}
.slider-dots span{width:5px;height:5px;border-radius:50%;background:#bbb}
.slider-dots span.active{background:#e07a1e}
.site-footer{position:absolute;left:0;top:1128px;width:1081px;height:72px;background:var(--footer)}
.copyright{position:absolute;left:127px;top:35px;transform:translateY(-50%);font-size:12px;color:var(--white)}
.social{position:absolute;left:769px;top:23px;display:flex;gap:8px}
.social span{width:24px;height:24px;border-radius:50%;background:var(--white)}
</style>
</head>
<body>
<header class="site-header">
  <a class="nav-link" style="left:257px">Home</a>
  <a class="nav-link" style="left:358px">About</a>
  <div class="brand">DRIFTING PAST SOLVANE</div>
  <a class="nav-link" style="left:745px">Testimonials</a>
  <a class="nav-link" style="left:878px">Contact</a>
</header>

<section class="hero"></section>
<div class="book-cover" role="img" aria-label="Book cover: silhouette of a man behind prison bars looking out to a tropical beach, with title and author name"></div>
<div class="shelf"></div>
<div class="shelf-peg" style="left:180px"></div>
<div class="shelf-peg" style="left:407px"></div>
<p class="hero-kicker">Now Available</p>
<h1 class="hero-title">DRIFTING PAST SOLVANE</h1>
<p class="hero-quote">” Lorem Ipsum is simply dummy text of the printing and typesetting industry. Lorem Ipsum has been the industry's standard dummy text ever since the 1500s, when an unknown printer took a galley of type and scrambled it to make a type specimen book. ”</p>
<a class="buy-button">BUY THE BOOK</a>

<h2 class="section-title" style="top:652px">About the Author</h2>
<p class="about-text">Lorem Ipsum is simply dummy text of the printing and typesetting industry. Lorem Ipsum has been the industry's standard dummy text ever since the 1500s, when an unknown printer took a galley of type and scrambled it to make a type specimen book. It has survived not only five centuries, but also the leap into electronic typesetting, remaining essentially unchanged. It was popularised in the 1960s with the release of Letraset sheets containing Lorem Ipsum passages, and more recently with desktop publishing software like Aldus PageMaker including versions of Lorem Ipsum.</p>
<div class="author-photo" role="img" aria-label="Portrait photo of the author"></div>

<div class="divider"></div>

<h2 class="section-title" style="top:925px">Testimonials</h2>
<div class="testimonial" style="left:128px">
  <div class="testimonial-photo" role="img" aria-label="Customer portrait photo"></div>
  <div class="testimonial-pointer"></div>
  <p class="testimonial-text">Lorem Ipsum is simply dummy text of the printing and typesetting industry lorem ipsum has been the industry's standard</p>
  <p class="testimonial-name">Customer Name</p>
</div>
<div class="testimonial" style="left:564px">
  <div class="testimonial-photo" role="img" aria-label="Customer portrait photo"></div>
  <div class="testimonial-pointer"></div>
  <p class="testimonial-text">Lorem Ipsum is simply dummy text of the printing and typesetting industry lorem ipsum has been the industry's standard</p>
  <p class="testimonial-name">Customer Name</p>
</div>
<div class="slider-dots"><span></span><span class="active"></span><span class="active"></span></div>

<footer class="site-footer">
  <p class="copyright">© 2014 DRIFTING PAST SOLVANE. All Rights Reserved.</p>
  <div class="social" aria-label="Social links">
    <span></span><span></span><span></span><span></span><span></span><span></span>
  </div>
</footer>
</body>
</html>
```